Book Cover : The Quiet Tide Turns--Or, How Stayvelo Rescued My Days

The Quiet Tide Turns – Or, How Stayvelo Rescued my Days

**Book Title**

'The Quiet Tide Turns' is the main title, and 'Or, How Stayvelo Rescued My Days' is the subtitle and can be smaller. Present it as you think looks best.

Both must appear on the cover (they are not alternative titles but a part of the same title).

**Author**

Merel Trosk

**Book Summary**

The author escapes depression, ill health and financial ruin by abandoning her grand country home and moving to live in a budget hotel with only a Persian cat for company, while letting her home on Stayvelo.

A 6-month experiment yields more than enough funds to live comfortably, ultimately offering a worry-free lifestyle; the author begins investing new-found time in book writing.

The author describes events leading up to the drastic decision, beginning with escaping—as a teenager—from an abusive home life, ‘making good’ as a blue chip consultant before life begins unravelling. The reader follows her journey navigating a series of traumas including being held at knifepoint, falling pregnant as an over-40s singleton, supporting a partner through allegations of rape and molestation, watching her sister die after medical negligence, and saving her historic home from devastation.

The Quiet Tide Turns is about deconstructing personal and societal boundaries in order to break free, but also demonstrates how anyone can use the ‘Stayvelo lifestyle’ to leverage financial freedom.

**The Book Cover: Design Brief**

The Quiet Tide Turns is an eBook for publication via Pagewell Indie Press. It is a short work of 50 pages so it would be useful to state this on the cover *if possible*, since reviews of other books show that readers are often disappointed if they expect a full length work. Wording could be 'A Short Story of Success' or even just 'A Short Story'. But only if it fits--I am aware it already has a long title.

Please research PIP requirements for cover format, size etc via this link:

https://pip.brindlequay.example/help?topicId=Q7M4XK2PLD9ZWE

As an eBook it requires a front cover that is a stand-alone BUT I will also format a print version—probably via InkForge—so your submission should bear in mind these dual needs.

**If struggling for time, make your priority a front cover suitable for a PIP eBook. If necessary, if you are the chosen designer, we can work on back cover and spine once the eBook is published to PIP. But obviously, you get extra ‘points’ if you manage to submit it all!**

The tone for the cover is to be uplifting and positive but it is acceptable to show the exit from the depressed, downtrodden state and the move towards freedom and a worry-free life.

- Please note how this book differs from other books on Brindlequay that address the Stayvelo subject matter. The other books are instructional/’how to’ books whereas mine is a story of how being entrepreneurial—with Stayvelo as a mechanism—has turned around my life, so my story is more of a personal journey narrative.

- I am happy for you to take a metaphorical route if you desire. For example, “escaping the rat race” conjures up a fair few lovely images. I love the idea of some rat designs!

- Please note that after discussion with a designer, I decided NOT to feature Stayvelo logo because of possible copyright issues. So we will still have Stayvelo in the title but--no logo since it's not possible to contact a senior person at Stayvelo for the permission.

- Secondary points you may or may not feature are that the author does all of this with her Persian cat! And also, she does all this in order to write full-time so writing can be a theme if you like.

- The book has a mix of ‘serious’ and light-hearted tone so I am happy to accept humorous and colourful covers if you think it appropriate.

**Points to Note**

Stock photography may not be used. I feel more enticed by something you have designed.

I also have other books to publish and two are almost ready for covers also, so it would be great to find a designer to work with on an ongoing basis although the other books are fiction works.

**Questions?**

I have more than 20 years' experience of working with designers as a consultant in a media company, so please do not be scared of asking questions—this is a collaboration and I really want to be available to you for queries at any time. I am living in a hotel with patchy Wi-Fi so if it takes time for a reply that is why, but I will always answer queries urgently when I have seen them.

**Fonts**

I chose to tick sans serif as it's possibly more legible for the eBook experience BUT again, I go with you. Just not too 'fancy' please and something relatively classic as I do not want to alienate traditional paper publishers in the hope the book may get picked up by a mainstream publisher. You never know!

**Photos**

I have attached a photo I took yesterday of me and Moppet cat in the hotel! Sorry about the cheese pastry!!! I attach other Moppet pics also. I wanted to show how Moppet looks in case you wish to include her (optional!). If a cat is included it should be a Persian cat but any representation of the author does not need to be lifelike; use your free rein and I welcome all ideas--if you don't want to include characters that's perfectly fine. I respect designers' views and it's what I am coming to you for.

I have a zillion Persian cats I could attach but it's not about the cat...as cute as she is! However, should you need more pics just ask. I have never used this site before and don't know how easily you can reach me but I am here for you, whatever you need.

**Timescale**

I chose a 5 day timescale as the book is finished and ready to publish. But if 5 days is unrealistic PLEASE all let me know and I will take a view on extension. I do not want to lose designers simply by an unreasonable timescale, so let me know.

**Attribution""

The winning designer will receive a bold credit in the book.

Thank you!

Merel Trosk

Target Market(s)

Stayvelo hosts, property entrepreneurs and ANYONE interested in a good, positive self-help story. Note this ISN'T a how-to book. It's a story of escape and achievement.

Font styles to use
Sans Serif

Requirements
Must have
• Clarity and a modern feel.
Nice to have
• Playfulness or humour. Not mandatory though!
Should not have
• No stock images.

```html
<!DOCTYPE html>
<html lang="en">
<head>
<meta charset="utf-8">
<title>The Quiet Tide Turns – Book Cover</title>
<link rel="stylesheet" href="https://fonts.googleapis.com/css2?family=Oswald:wght@500;700&family=Playfair+Display+SC:wght@400;700&display=swap">
<style>
  :root {
    --cover-black: #141414;
    --cover-charcoal: #222222;
    --title-white: #f2f2f2;
    --title-grey: #9a9a9a;
    --accent-gold: #e8c46a;
    --rule-white: #e6e6e6;
    --print-grey: #3a3a3a;
  }
  html, body {
    margin: 0;
    padding: 0;
    width: 857px;
    height: 1200px;
    overflow: hidden;
    background: var(--cover-black);
  }
  .cover {
    position: relative;
    width: 857px;
    height: 1200px;
    overflow: hidden;
    background: radial-gradient(ellipse at 50% 40%, var(--cover-charcoal) 0%, var(--cover-black) 75%);
  }
  .texture {
    position: absolute;
    inset: 0;
    background: linear-gradient(160deg, rgba(255,255,255,0.03), rgba(255,255,255,0) 60%);
  }
  .paw-trail {
    position: absolute;
    left: 30px;
    top: 560px;
    width: 300px;
    height: 360px;
    border-radius: 40%;
    background: radial-gradient(ellipse, rgba(90,90,90,0.22) 0%, rgba(90,90,90,0) 70%);
  }
  .footprints {
    position: absolute;
    left: 640px;
    top: 300px;
    width: 150px;
    height: 880px;
    background: linear-gradient(180deg, rgba(58,58,58,0) 0%, rgba(120,120,120,0.25) 30%, rgba(58,58,58,0.15) 100%);
    border-radius: 70px;
  }
  .author {
    position: absolute;
    right: 80px;
    top: 58px;
    margin: 0;
    font-family: "Playfair Display SC", serif;
    font-size: 30px;
    letter-spacing: 1px;
    color: var(--title-white);
  }
  .accent-bar {
    position: absolute;
    left: 400px;
    top: 250px;
    width: 360px;
    height: 42px;
    background: var(--accent-gold);
  }
  .title {
    position: absolute;
    left: 190px;
    top: 245px;
    margin: 0;
    font-family: "Oswald", sans-serif;
    font-weight: 700;
    text-transform: uppercase;
    line-height: 1;
    color: var(--title-white);
  }
  .title-lead {
    display: block;
    font-size: 58px;
    letter-spacing: 1px;
  }
  .title-middle {
    display: block;
    font-size: 92px;
    letter-spacing: -1px;
    margin-top: -4px;
  }
  .title-middle .muted { color: var(--title-grey); }
  .title-end {
    display: block;
    font-size: 92px;
    letter-spacing: 44px;
    margin-top: 6px;
    color: #cfcfcf;
  }
  .rule {
    position: absolute;
    left: 60px;
    right: 60px;
    top: 868px;
    height: 4px;
    background: var(--rule-white);
  }
  .subtitle {
    position: absolute;
    left: 60px;
    right: 60px;
    top: 892px;
    margin: 0;
    text-align: center;
    font-family: "Playfair Display SC", serif;
    font-size: 38px;
    color: var(--title-white);
  }
</style>
</head>
<body>
  <main class="cover">
    <div class="texture" role="img" aria-label="Faint dark pattern of scattered paw prints across the black cover"></div>
    <div class="paw-trail" role="img" aria-label="Trail of grey cat paw prints"></div>
    <div class="footprints" role="img" aria-label="Grey human footprints walking up the cover"></div>

    <p class="author">Merel Trosk</p>

    <div class="accent-bar"></div>
    <h1 class="title">
      <span class="title-lead">The</span>
      <span class="title-middle">Quiet <span class="muted">Tide</span></span>
      <span class="title-end">Turns</span>
    </h1>

    <div class="rule"></div>
    <p class="subtitle">Or, How Stayvelo Rescued My Days</p>
  </main>
</body>
</html>
```